Tobin's Butter dairy product for export market

We are starting a new brand for our butter range. We are looking for a premimum branding with family values. The product should be elligent and simle and easy for consumers to choose and easy for chefs,

A samples of our current brand and packing details in on the pack
target markets , China, Hong Kong, Asia, middle east
products will be sold in different size starting from small portion eg 7g to 1kg food service pack
product will be sold in 2 varients salted and unsalted

Target Market(s)

Australian Market and export market

Industry/Entity Type

Product

Colors
9bcb3c
fbed22

Requirements
Must have
• Pure butter
• packed in Australia
• nice fresh modern simple design
Nice to have
• Colours gold , green or any other suggestions welcome.
Should not have
• Any third party pictures of butter etc..

```html
<!DOCTYPE html>
<html lang="en">
<head>
<meta charset="utf-8">
<title>Tobin's Butter – Pack Fronts</title>
<link href="https://fonts.googleapis.com/css2?family=Encode+Sans+Semi+Condensed:wght@400;500;600&display=swap" rel="stylesheet">
<style>
  :root{
    --bg:#ffffff;
    --panel-white:#eeeef2;
    --navy:#1f3c93;
    --sky:#18a4e4;
    --green-dark:#1f7a2c;
    --green:#3f9d2f;
    --brand-green:#9bcb3c;
    --silver-1:#a9adb6;
    --silver-2:#e4e6ea;
    --gold-1:#c9a227;
    --gold-2:#f6ea8a;
    --ink-soft:#555a60;
  }
  *{box-sizing:border-box;margin:0;padding:0}
  html,body{width:1200px;height:1200px;overflow:hidden;background:var(--bg)}
  body{font-family:"Encode Sans Semi Condensed",Arial,sans-serif;position:relative}

  .pack-front{position:absolute;left:100px;width:1000px;height:480px;overflow:hidden;box-shadow:0 10px 30px rgba(0,0,0,.18)}
  .pack-front--unsalted{top:90px}
  .pack-front--salted{top:630px}
  .pack-art{position:absolute;inset:0;width:100%;height:100%}

  .brand{position:absolute;left:40px;top:275px;height:80px;display:flex;align-items:center;gap:18px}
  .brand-dot{width:80px;height:80px;border-radius:50%;background:var(--brand-green);flex:none}
  .brand-name{font-size:44px;font-weight:600;line-height:1;color:var(--green-dark);white-space:nowrap}

  .claims{position:absolute;left:560px;top:142px;width:400px;text-align:center}
  .claims-line{font-size:24px;font-weight:400;line-height:1.2}
  .variant{font-size:76px;font-weight:600;line-height:.95;margin-top:8px;letter-spacing:-1px;white-space:nowrap}
  .descriptor{font-size:44px;font-weight:400;line-height:1.05;white-space:nowrap}
  .pack-front--unsalted .claims{color:var(--navy)}
  .pack-front--salted .claims{color:var(--green-dark)}

  .net-weight{position:absolute;right:50px;top:348px;font-size:20px;line-height:1;color:var(--ink-soft)}

  .badge{position:absolute;border-radius:50%;border:3px solid var(--navy);background:#fff}
  .pack-front--salted .badge{border-color:var(--green-dark)}
  .badge--origin{right:60px;top:36px;width:92px;height:92px}
  .badge--cert-a{left:40px;bottom:40px;width:62px;height:62px}
  .badge--cert-b{left:116px;bottom:40px;width:62px;height:62px}
</style>
</head>
<body>

<section class="pack-front pack-front--unsalted">
  <svg class="pack-art" viewBox="0 0 1000 480" preserveAspectRatio="none" aria-hidden="true">
    <defs>
      <linearGradient id="silver" x1="0" y1="0" x2="1" y2="1">
        <stop offset="0" stop-color="var(--silver-1)"/>
        <stop offset=".5" stop-color="var(--silver-2)"/>
        <stop offset="1" stop-color="var(--silver-1)"/>
      </linearGradient>
    </defs>
    <rect width="1000" height="480" fill="url(#silver)"/>
    <path d="M0 260 C300 220 650 70 1000 10 L1000 390 C700 380 300 400 0 460 Z" fill="var(--panel-white)"/>
    <path d="M0 260 C300 220 650 70 1000 10" fill="none" stroke="var(--sky)" stroke-width="18"/>
    <path d="M0 460 C300 400 700 380 1000 390" fill="none" stroke="var(--sky)" stroke-width="16"/>
    <path d="M0 478 C320 420 700 400 1000 410" fill="none" stroke="var(--navy)" stroke-width="8"/>
  </svg>
  <div class="badge badge--origin"></div>
  <div class="brand"><span class="brand-dot"></span><span class="brand-name">Tobin's Butter</span></div>
  <div class="claims">
    <p class="claims-line">NO PRESERVATIVES</p>
    <p class="claims-line">NO VEGETABLE FATS</p>
    <p class="variant">UNSALTED</p>
    <p class="descriptor">PURE BUTTER</p>
  </div>
  <p class="net-weight">1kg NET</p>
  <div class="badge badge--cert-a"></div>
  <div class="badge badge--cert-b"></div>
</section>

<section class="pack-front pack-front--salted">
  <svg class="pack-art" viewBox="0 0 1000 480" preserveAspectRatio="none" aria-hidden="true">
    <defs>
      <linearGradient id="gold" x1="0" y1="0" x2="1" y2="1">
        <stop offset="0" stop-color="var(--gold-1)"/>
        <stop offset=".55" stop-color="var(--gold-2)"/>
        <stop offset="1" stop-color="var(--gold-1)"/>
      </linearGradient>
    </defs>
    <rect width="1000" height="480" fill="url(#gold)"/>
    <path d="M0 260 C300 220 650 70 1000 10 L1000 390 C700 380 300 400 0 460 Z" fill="var(--panel-white)"/>
    <path d="M0 260 C300 220 650 70 1000 10" fill="none" stroke="var(--green-dark)" stroke-width="18"/>
    <path d="M0 460 C300 400 700 380 1000 390" fill="none" stroke="var(--green)" stroke-width="16"/>
    <path d="M0 478 C320 420 700 400 1000 410" fill="none" stroke="var(--green-dark)" stroke-width="8"/>
  </svg>
  <div class="badge badge--origin"></div>
  <div class="brand"><span class="brand-dot"></span><span class="brand-name">Tobin's Butter</span></div>
  <div class="claims">
    <p class="claims-line">NO PRESERVATIVES</p>
    <p class="claims-line">NO VEGETABLE FATS</p>
    <p class="variant">SALTED</p>
    <p class="descriptor">PURE BUTTER</p>
  </div>
  <p class="net-weight">1kg NET</p>
  <div class="badge badge--cert-a"></div>
  <div class="badge badge--cert-b"></div>
</section>

</body>
</html>
```